Voyage and Sail Halvora 2017

I need cover design and catalog/brochure layout for a deluxe trip.
The itinerary pages my contain 3 columns with information on the trip and color images ( column1 photo/ column2 destination description/column 3photo)
The graphic layout is most important and it needs to be in a double sided catalog format.
the project needs to use a common publishing software that can be imported into Microsoft Word or Apple Pages - this will allow me to enter the content

Target Market(s)

upscale travelers

Industry/Entity Type

Travel

Font styles to use
Serif

Requirements
Must have
• -very classy look and feel that appeals to experienced travelers 40 and older
• - layout that can be imported as a template in MS Word or Apple Pages
Nice to have
• Major improvement in layout and graphic design
Should not have
• project must not look like it was done by me! - professional appearance is paramount

```html
<!DOCTYPE html>
<html lang="en">
<head>
<meta charset="utf-8">
<title>Voyage and Sail Halvora 2017 – Brochure Spread</title>
<link rel="stylesheet" href="https://fonts.googleapis.com/css2?family=Anton&family=Tinos:wght@400;700&display=swap">
<style>
  :root{
    --backdrop:#e4e4e4;
    --paper:#ececec;
    --green:#137334;
    --red:#d81f26;
    --ink:#0a0a0a;
    --gold:#f2e600;
    --gold-light:#fffbd0;
    --white:#ffffff;
    --photo-sky:#c7a57a;
    --photo-town:#8a5a3a;
    --photo-river:#3f5058;
    --map-olive:#4a4a2a;
  }
  html,body{margin:0;padding:0;width:1200px;height:893px;overflow:hidden;background:var(--backdrop);}
  .spread{position:absolute;left:63px;top:66px;width:1074px;height:760px;display:flex;box-shadow:0 14px 30px rgba(0,0,0,.18);}
  .page{position:relative;width:537px;height:760px;overflow:hidden;}

  /* Left page: highlights */
  .page--highlights{background:var(--paper);}
  .hero-photo{position:absolute;left:0;top:0;width:537px;height:330px;
    background:linear-gradient(180deg,#8fa6b8 0%,var(--photo-sky) 28%,var(--photo-town) 55%,#6b4a35 72%,var(--photo-river) 100%);}
  .highlights-ribbon{position:absolute;left:0;top:300px;width:300px;height:62px;}
  .highlights-title{position:absolute;left:22px;top:312px;margin:0;font:400 27px/1 "Tinos",serif;color:var(--white);letter-spacing:.5px;}
  .highlight-list{position:absolute;left:0;top:392px;width:537px;margin:0;padding:0;list-style:none;}
  .highlight{position:absolute;height:60px;border-radius:30px;display:flex;align-items:center;justify-content:center;text-align:center;
    font:700 15px/1.2 "Tinos",serif;color:var(--white);padding:0 24px;box-sizing:border-box;}
  .highlight--green{background:var(--green);}
  .highlight--red{background:var(--red);}

  /* Right page: cover */
  .page--cover{background:var(--ink);}
  .cover-bands{position:absolute;inset:0;}
  .map-area{position:absolute;left:150px;top:150px;width:250px;height:520px;border-radius:46% 40% 38% 44%/20% 18% 22% 20%;
    background:radial-gradient(ellipse at 50% 40%,#6b6b40 0%,var(--map-olive) 55%,#1e1e12 100%);opacity:.85;}
  .dancer-art{position:absolute;left:236px;top:410px;width:80px;height:120px;border-radius:40% 40% 30% 30%;
    background:radial-gradient(ellipse at 50% 40%,#b02a2a 0%,#5a1414 60%,#151515 100%);}
  .boat-art{position:absolute;left:70px;top:560px;width:390px;height:72px;border-radius:8px 8px 30px 30px;
    background:linear-gradient(180deg,#d8d2c0 0%,#8a4a28 45%,#5a2a16 100%);}
  .cover-title{position:absolute;left:0;top:168px;width:537px;text-align:center;margin:0;}
  .cover-title__place{display:block;font:400 104px/1 "Anton",sans-serif;letter-spacing:1px;
    background:linear-gradient(180deg,var(--gold-light) 0%,var(--gold) 55%,#c9b800 100%);
    -webkit-background-clip:text;background-clip:text;color:transparent;
    filter:drop-shadow(3px 4px 0 #3a3a00);}
  .cover-title__sub{display:block;margin-top:4px;font:400 38px/1 "Anton",sans-serif;color:var(--gold);
    text-shadow:2px 3px 0 #3a3a00;}
  .cover-dates{position:absolute;left:0;top:640px;width:537px;text-align:center;margin:0;
    font:400 24px/1 "Tinos",serif;color:var(--white);}
  .cover-dates__day{color:var(--gold);}
</style>
</head>
<body>
<main class="spread">
  <section class="page page--highlights">
    <div class="hero-photo" role="img" aria-label="Sunset view of a riverside old town with terracotta roofs and moored boats"></div>
    <svg class="highlights-ribbon" viewBox="0 0 300 62" aria-hidden="true">
      <polygon points="0,0 262,0 300,31 262,62 0,62" fill="var(--red)"/>
      <polyline points="0,58 255,58 290,31" fill="none" stroke="var(--white)" stroke-width="2"/>
    </svg>
    <h2 class="highlights-title">HIGHLIGHTS</h2>
    <ul class="highlight-list">
      <li class="highlight highlight--green" style="left:150px;top:0;width:360px;">12 Days and 11 Nights Unique and Exclusive Itinerary Voyage and Sail in Halvora</li>
      <li class="highlight highlight--red" style="left:110px;top:72px;width:360px;">17 Guided Tours of Famous and Historical Sites</li>
      <li class="highlight highlight--green" style="left:70px;top:144px;width:360px;">Sail on Lady Marisol's "Spirit of Corwen" Yacht through the beautiful Velmora Valley Cruise</li>
      <li class="highlight highlight--red" style="left:40px;top:216px;width:360px;">Fado &amp; Flamenco Shows</li>
      <li class="highlight highlight--green" style="left:20px;top:288px;width:360px;">Cuisine and Wine Special Events</li>
    </ul>
  </section>

  <section class="page page--cover">
    <svg class="cover-bands" viewBox="0 0 537 760" aria-hidden="true">
      <rect x="0" y="0" width="537" height="96" fill="var(--green)"/>
      <polygon points="250,96 290,62 537,62 537,130 250,130" fill="var(--red)"/>
      <polyline points="0,96 250,96 290,62 537,62" fill="none" stroke="var(--white)" stroke-width="3"/>
      <line x1="0" y1="130" x2="537" y2="130" stroke="var(--white)" stroke-width="3"/>
      <rect x="0" y="670" width="537" height="90" fill="var(--green)"/>
      <polygon points="0,670 537,670 537,700 280,700 245,728 0,728" fill="var(--red)"/>
      <line x1="0" y1="670" x2="537" y2="670" stroke="var(--white)" stroke-width="3"/>
      <polyline points="0,728 245,728 280,700 537,700" fill="none" stroke="var(--white)" stroke-width="3"/>
    </svg>
    <div class="map-area" role="img" aria-label="Relief map of the country in olive tones"></div>
    <div class="dancer-art" role="img" aria-label="Flamenco dancer in a red dress"></div>
    <div class="boat-art" role="img" aria-label="Cruise yacht on the river"></div>
    <h1 class="cover-title">
      <span class="cover-title__place">Halvora</span>
      <span class="cover-title__sub">Voyage &amp; Sail</span>
    </h1>
    <p class="cover-dates">October <span class="cover-dates__day">24th</span> to November <span class="cover-dates__day">4th 2017</span></p>
  </section>
</main>
</body>
</html>
```